Business Card Design Project

We require a business card template to cover basic contact information - our company logo, names of employees, title, mobile and email.

Target Market(s)

Corporate

Industry/Entity Type

Business

Font styles to use
Sans Serif

Requirements
Nice to have
• Thinking it would be great just to have the logo taking up approximately half the space (so it goes as far across the top of the card as possible) and then contact details in the lower half of the card. Keen just to use only the two colours in the logo, on a white background.
Should not have
• No fussy drawings

```html
<!DOCTYPE html>
<html lang="en">
<head>
<meta charset="UTF-8">
<title>Tidewell Developments – Business Card</title>
<link rel="stylesheet" href="https://fonts.googleapis.com/css2?family=Arimo:wght@400&display=swap">
<style>
  :root {
    --teal: #33a5b9;
    --blue: #2e66a8;
    --white: #ffffff;
  }
  * { margin: 0; padding: 0; box-sizing: border-box; }
  html, body {
    width: 1200px;
    height: 703px;
    overflow: hidden;
    background: var(--white);
  }
  .card {
    position: relative;
    width: 1200px;
    height: 703px;
    background: var(--white);
    font-family: "Arimo", Arial, sans-serif;
    font-weight: 400;
  }
  .wordmark {
    position: absolute;
    left: 0;
    right: 0;
    top: 40px;
    text-align: center;
    color: var(--teal);
    line-height: 1;
  }
  .wordmark-name {
    display: block;
    font-size: 210px;
    letter-spacing: -4px;
  }
  .wordmark-sub {
    display: block;
    font-size: 52px;
    margin-top: 8px;
    padding-left: 520px;
  }
  .person {
    position: absolute;
    left: 0;
    right: 0;
    top: 404px;
    text-align: center;
    color: var(--blue);
  }
  .person-name {
    font-size: 52px;
    line-height: 1.1;
  }
  .person-title {
    font-size: 40px;
    line-height: 1.1;
    margin-top: 6px;
  }
  .contact-band {
    position: absolute;
    left: 0;
    right: 0;
    top: 573px;
    bottom: 0;
    background: var(--teal);
    color: var(--white);
    font-size: 34px;
  }
  .contact-phone {
    position: absolute;
    left: 65px;
    top: 14px;
    line-height: 58px;
  }
  .contact-divider {
    position: absolute;
    left: 598px;
    top: 34px;
    width: 5px;
    height: 60px;
    background: var(--white);
  }
  .contact-email {
    position: absolute;
    right: 64px;
    top: 42px;
    line-height: 44px;
  }
</style>
</head>
<body>
  <div class="card">
    <div class="wordmark">
      <span class="wordmark-name">Tidewell</span>
      <span class="wordmark-sub">developments</span>
    </div>

    <div class="person">
      <p class="person-name">(Names of Employees)</p>
      <p class="person-title">title</p>
    </div>

    <div class="contact-band">
      <div class="contact-phone">
        <p>Mobil Number</p>
        <p>Fax</p>
      </div>
      <div class="contact-divider"></div>
      <p class="contact-email">Email address</p>
    </div>
  </div>
</body>
</html>
```